Classic Minimalistic Business Card

Design a classic, minimalistic Business Card. Please find inspiration in the attached Classic Minimalistic examples. My information:
Name: Glen Ovamir
Company: Ovamir Capital
Logo: OC
Address: 1470 N Thornwick Rd, Suite 210 | Larkfield, IL 60599
Phone: 630-555-0192
Email: glenovamir@pvt.insure
Slogan: Building Strength Through Capital

Feel free to leave out any of the information above except my name.

I have selected Double-sided, but I am also open to Single-sided

Target Market(s)

22-70. income greater than 150k/year

Industry/Entity Type

Finance

Contact Information for Business Card

See Project Description

Requirements
Must have
• Ivory or "antiqued" background similar to the reference pictures

```html
<!DOCTYPE html>
<html lang="en">
<head>
<meta charset="utf-8">
<title>Ovamir Capital — Business Card</title>
<link rel="stylesheet" href="https://fonts.googleapis.com/css2?family=Josefin+Sans:wght@400;600&display=swap">
<style>
  :root {
    --page-bg: #ebebeb;
    --card-stock: #c9b692;
    --ink: #141210;
    --card-shadow: rgba(0, 0, 0, 0.22);
  }
  * { box-sizing: border-box; margin: 0; padding: 0; }
  html, body {
    width: 1200px;
    height: 900px;
    overflow: hidden;
    background: var(--page-bg);
  }
  .business-card {
    position: absolute;
    left: 100px;
    top: 164px;
    width: 1000px;
    height: 572px;
    background: var(--card-stock);
    color: var(--ink);
    font-family: "Josefin Sans", sans-serif;
    box-shadow: 0 10px 28px var(--card-shadow);
  }
  .brand {
    position: absolute;
    top: 150px;
    left: 0;
    width: 1000px;
    display: flex;
    align-items: center;
    justify-content: center;
    gap: 18px;
    padding-left: 60px;
  }
  .brand-mark {
    width: 40px;
    height: 40px;
    border-radius: 50%;
    background: var(--ink);
  }
  .brand-name {
    font-size: 32px;
    font-weight: 400;
    letter-spacing: 0.14em;
    line-height: 1;
    padding-top: 6px;
  }
  .holder-name {
    position: absolute;
    top: 352px;
    right: 560px;
    font-size: 31px;
    font-weight: 600;
    letter-spacing: 0.04em;
    text-transform: uppercase;
    white-space: nowrap;
  }
  .divider {
    position: absolute;
    left: 460px;
    top: 311px;
    width: 2px;
    height: 116px;
    background: var(--ink);
  }
  .contact {
    position: absolute;
    left: 488px;
    top: 314px;
    font-style: normal;
    letter-spacing: 0.06em;
    white-space: nowrap;
  }
  .contact-line {
    display: block;
    font-size: 18px;
    line-height: 27px;
  }
  .contact-line.address { font-variant: small-caps; }
  .contact-line.phone { margin-top: 6px; }
  .contact-line.email {
    font-size: 15px;
    text-transform: uppercase;
    margin-top: 2px;
  }
  .slogan {
    position: absolute;
    top: 498px;
    left: 0;
    width: 960px;
    text-align: center;
    font-size: 17px;
    letter-spacing: 0.3em;
    text-transform: uppercase;
  }
</style>
</head>
<body>
  <article class="business-card">
    <header class="brand">
      <span class="brand-mark"></span>
      <span class="brand-name">OVAMIR CAPITAL</span>
    </header>

    <h1 class="holder-name">Glen Ovamir</h1>
    <div class="divider"></div>

    <address class="contact">
      <span class="contact-line address">1470 N Thornwick Rd, Suite 210</span>
      <span class="contact-line address">Larkfield, IL 60599</span>
      <span class="contact-line phone">630-555-0192</span>
      <span class="contact-line email">glenovamir@pvt.insure</span>
    </address>

    <p class="slogan">Building Strength Through Capital</p>
  </article>
</body>
</html>
```